Wall wrap design. Automotive shop with high end luxury feel.

I have a car wrap shop that does some really cool car wraps on every brand cars. Cars like Vornik all they way up to Caldrens, Fenzavetti, Moravelle etc…

Looking for a design that could be very minimal, modern, or loud and eye catching. The wall is huge where cars we work on will be infront of it. A lot of picture will be taken of it. There will be 6 tv on the wall

Can be car related or eye catching art

```html
<!DOCTYPE html>
<html lang="en">
<head>
<meta charset="utf-8">
<title>Halvane Wall Wrap</title>
<link rel="stylesheet" href="https://fonts.googleapis.com/css2?family=Exo+2:wght@800&display=swap">
<style>
  :root {
    --backdrop: #4a4a4a;
    --paper: #ffffff;
    --cream: #f8ecd2;
    --navy: #172f4f;
    --wine: #7c1a20;
    --signal-red: #d12f34;
    --rose-red: #d42a40;
    --ocean: #1c78ba;
    --brand-red: #e0383e;
  }
  html, body {
    margin: 0;
    padding: 0;
    width: 1200px;
    height: 374px;
    overflow: hidden;
    background: var(--backdrop);
  }
  .wall-wrap {
    display: block;
    width: 1200px;
    height: 374px;
  }
  .panel { fill: var(--paper); }
  .ray-cream { fill: var(--cream); }
  .ray-navy { fill: var(--navy); }
  .ray-wine { fill: var(--wine); }
  .ray-red { fill: var(--rose-red); }
  .band-red { fill: var(--signal-red); }
  .band-blue { fill: var(--ocean); }
  .brand-name {
    font-family: "Exo 2", sans-serif;
    font-weight: 800;
    font-size: 23px;
    fill: var(--brand-red);
    letter-spacing: -0.5px;
  }
</style>
</head>
<body>
<svg class="wall-wrap" viewBox="0 0 1926 600" preserveAspectRatio="none" xmlns="http://www.w3.org/2000/svg">
  <defs>
    <linearGradient id="wrap-chrome" x1="0" y1="0" x2="1" y2="1">
      <stop offset="0" stop-color="#a89a3c"/>
      <stop offset="0.45" stop-color="#9a55b8"/>
      <stop offset="1" stop-color="#4a4fb0"/>
    </linearGradient>
    <linearGradient id="wrap-art" x1="0" y1="0" x2="1" y2="1">
      <stop offset="0" stop-color="#2b2f6e"/>
      <stop offset="0.6" stop-color="#5a5fa8"/>
      <stop offset="1" stop-color="#7a2a40"/>
    </linearGradient>
  </defs>

  <rect class="panel" x="112" y="107" width="1701" height="386"/>

  <g class="bursts">
    <polygon class="ray-cream" points="130,107 320,107 480,232"/>
    <polygon class="ray-navy" points="528,107 640,107 528,230"/>
    <polygon class="ray-wine" points="615,215 740,135 915,140"/>
    <polygon class="band-red" points="620,258 1000,200 1425,107 1813,107 1813,298 1300,290 900,275"/>
    <polygon class="band-blue" points="728,300 1150,330 1813,408 1813,493 1270,493"/>
    <polygon class="ray-cream" points="600,340 990,493 740,493"/>
    <polygon class="ray-red" points="430,360 540,350 557,443 365,438"/>
    <polygon class="ray-wine" points="112,390 345,368 205,493 112,493"/>
  </g>

  <g class="brand-pennant">
    <polygon class="ray-navy" points="172,203 390,258 172,300"/>
    <text class="brand-name" x="205" y="262">Halvane</text>
  </g>

  <rect role="img" aria-label="Photo of a sports coupe in a blue and red art wrap"
        x="348" y="250" width="264" height="108" rx="40" fill="url(#wrap-art)"/>
  <rect role="img" aria-label="Photo of a race car with rear wing in a gold-to-purple colour-shift wrap"
        x="790" y="150" width="636" height="290" rx="90" fill="url(#wrap-chrome)"/>
</svg>
</body>
</html>
```